Fence Flyer to Attract More Sales During Winter

We need a new flyer made that we can distribute to residential mailboxes. The flyer is to promote our Frostline Picket Days. We like simply designs, and we would like the flyer to showcase a lot of our fence photos. More of our photos are online at our website at www.getbramblerail.com - our new address needs to also be featured on the flyer - 436 Quillen rd, Monroe, NC 28117. I do want the words "FROSTLINE PICKET DAYS" to be dominate on the flyer with the description "Wood fences starting at $12/FT!" Please look through our Facebook page and our website to gather more photos or information. We are flexible on colors, nothing to fancy - simple flyer design please.

Target Market(s)

Residential homeowners that need a new fence to enclose their yard for safety, security or decorative

Industry/Entity Type

Residential Construction

Font styles to use
Sans Serif

Colors

Designer to choose colors to be used in the design.

Requirements
Must have
• Frostline Picket Days
• Contact information for the business
• "Come visit our outdoor showroom, open 24/7!"
Nice to have
• Photos of our fences - you can find more on our website at www.GetBrambleRail.com or Facebook.com/MeadowlarkRailGPV
Should not have
• Flashy designs

```html
<!DOCTYPE html>
<html lang="en">
<head>
<meta charset="utf-8">
<title>Bramble Rail Fence – Frostline Picket Days</title>
<link href="https://fonts.googleapis.com/css2?family=Anton&family=Arimo:wght@700&family=Saira+Semi+Condensed:wght@600&display=swap" rel="stylesheet">
<style>
  :root{
    --brown:#583c2a;
    --orange:#e38e38;
    --blue:#3e86c8;
    --tan:#936a4c;
    --ink:#111;
    --paper:#fff;
    --band:#000;
  }
  html,body{margin:0;padding:0;overflow:hidden;background:var(--paper);}
  .flyer{position:relative;width:927px;height:1200px;overflow:hidden;background:var(--paper);font-family:"Arimo",Arial,sans-serif;}

  /* brand block */
  .brand-mark{position:absolute;left:300px;top:72px;width:56px;height:56px;background:var(--brown);}
  .brand-name{position:absolute;left:384px;top:68px;font:700 29px/1 "Arimo",Arial,sans-serif;color:var(--blue);}
  .brand-phone{position:absolute;left:384px;top:106px;font:700 29px/1 "Arimo",Arial,sans-serif;color:var(--ink);}
  .brand-tagline{position:absolute;left:385px;top:148px;font:700 10.5px/1 "Arimo",Arial,sans-serif;color:var(--ink);}

  /* headline */
  .headline{position:absolute;left:0;width:100%;top:196px;text-align:center;font:400 77px/1.1 "Anton",Impact,sans-serif;letter-spacing:3px;color:var(--brown);margin:0;}
  .offer{position:absolute;left:0;width:100%;top:282px;text-align:center;font:400 44px/1.1 "Anton",Impact,sans-serif;letter-spacing:2.5px;color:var(--blue);margin:0;}
  .showroom{position:absolute;left:0;width:100%;top:346px;text-align:center;font:600 45px/1.1 "Saira Semi Condensed",sans-serif;color:var(--ink);margin:0;}

  /* diamond tiles */
  .tile{position:absolute;border-radius:16px;transform:rotate(45deg);
    left:calc(var(--cx) - var(--s) / 2);top:calc(var(--cy) - var(--s) / 2);width:var(--s);height:var(--s);}
  .tile--orange{background:var(--orange);}
  .tile--brown{background:var(--brown);}
  .tile--blue{background:var(--blue);}
  .tile--tan{background:var(--tan);}
  .photo--metal{background:linear-gradient(135deg,#6f8f4a 0%,#2b2f22 45%,#79a34c 100%);}
  .photo--wood{background:linear-gradient(135deg,#4f6b39 0%,#d3a66e 45%,#e2bb84 100%);}
  .photo--picket{background:linear-gradient(135deg,#7a5737 0%,#e1b985 50%,#8a6443 100%);}

  .tile-label{position:absolute;font:700 31px/1.25 "Arimo",Arial,sans-serif;letter-spacing:3px;text-align:center;margin:0;}
  .tile-label--alu{left:183px;width:200px;top:527px;color:var(--ink);}
  .tile-label--wood{left:564px;width:200px;top:780px;color:var(--paper);font-size:34px;}
  .tile-label--trash{left:48px;top:918px;color:var(--paper);font-size:26px;letter-spacing:0.5px;text-align:left;line-height:1.5;}

  .address{position:absolute;left:120px;width:300px;top:1082px;text-align:center;font:700 24px/1.75 "Arimo",Arial,sans-serif;color:var(--ink);margin:0;}
  .pin{position:absolute;left:259px;top:1020px;width:28px;height:44px;}

  .web-band{position:absolute;left:389px;top:1127px;width:538px;height:73px;background:var(--band);clip-path:polygon(72px 0,100% 0,100% 100%,0 100%);}
  .web-icon{position:absolute;left:489px;top:1146px;width:23px;height:23px;}
  .web-url{position:absolute;left:525px;top:1143px;font:700 24.5px/1 "Arimo",Arial,sans-serif;color:var(--paper);}
</style>
</head>
<body>
<main class="flyer">
  <header>
    <div class="brand-mark" aria-hidden="true"></div>
    <div class="brand-name">Bramble Rail Fence</div>
    <div class="brand-phone">704-555-0148</div>
    <div class="brand-tagline">“Because Good Fences Make Good Neighbors”</div>
  </header>

  <h1 class="headline">FROSTLINE PICKET DAYS</h1>
  <p class="offer">Wood fences starting at $12/FT!</p>
  <p class="showroom">come visit our outdoor showroom, open 24/7!</p>

  <section class="gallery">
    <div class="tile photo--metal" style="--cx:90px;--cy:657px;--s:191px" role="img" aria-label="Black aluminum fence beside a garden path with flowering shrubs"></div>
    <div class="tile tile--orange" style="--cx:282px;--cy:555px;--s:171px"></div>
    <div class="tile photo--wood" style="--cx:636px;--cy:553px;--s:174px" role="img" aria-label="Tall wooden privacy fence with gate in front of a shed"></div>
    <div class="tile photo--metal" style="--cx:464px;--cy:693px;--s:192px" role="img" aria-label="Black aluminum fence with spear tops along a white building"></div>
    <div class="tile photo--metal" style="--cx:840px;--cy:661px;--s:195px" role="img" aria-label="Black aluminum fence and gate across a green lawn"></div>
    <div class="tile photo--picket" style="--cx:249px;--cy:824px;--s:196px" role="img" aria-label="Close view of a natural wood picket fence over mulch"></div>
    <div class="tile tile--brown" style="--cx:666px;--cy:829px;--s:208px"></div>
    <div class="tile tile--blue" style="--cx:76px;--cy:966px;--s:194px"></div>
    <div class="tile photo--wood" style="--cx:463px;--cy:982px;--s:192px" role="img" aria-label="Long arched-top wooden privacy fence along a yard"></div>
    <div class="tile photo--metal" style="--cx:881px;--cy:962px;--s:194px" role="img" aria-label="Black aluminum fence running down a grassy slope"></div>
    <div class="tile photo--wood" style="--cx:681px;--cy:1142px;--s:229px" role="img" aria-label="Wooden trash enclosure with black gate hardware"></div>
    <div class="tile tile--tan" style="--cx:228px;--cy:1165px;--s:277px"></div>

    <p class="tile-label tile-label--alu">Aluminum<br>Fence</p>
    <p class="tile-label tile-label--wood">Wood<br>Fence</p>
    <p class="tile-label tile-label--trash">Trash<br>Enclosure</p>
  </section>

  <svg class="pin" viewBox="0 0 28 44" aria-hidden="true">
    <path d="M14 0C6.3 0 0 6.2 0 14c0 9 14 30 14 30s14-21 14-30C28 6.2 21.7 0 14 0z" fill="#111"/>
    <circle cx="14" cy="14" r="6" fill="var(--tan)"/>
  </svg>
  <p class="address">436 Quillen rd,<br>Monroe, NC 28117</p>

  <footer>
    <div class="web-band"></div>
    <svg class="web-icon" viewBox="0 0 24 24" aria-hidden="true" fill="none" stroke="#fff" stroke-width="1.6">
      <circle cx="12" cy="12" r="10.5"/>
      <ellipse cx="12" cy="12" rx="4.5" ry="10.5"/>
      <line x1="1.5" y1="12" x2="22.5" y2="12"/>
      <path d="M3.5 6.5h17M3.5 17.5h17"/>
    </svg>
    <div class="web-url">www.GetBrambleRail.com</div>
  </footer>
</main>
</body>
</html>
```